Website for keystone mobile detailing.

Need a homepage, pages for: car and truck detailing, boat detailing, airplane detailing, about us, contact us. I have the domain name through nimbuspark so I will need the design uploaded on my domain. Also hoping to link other domains to this page.I would like to see the logo more pronounced. I would like to see a large phone number link to call my business. The layout looks nice but the pics need to depict car washing and waxing not car mechanics. i would like the colors of the webpage to incorporate the colors found in the logo in some way. I would like links to social media pages

Target Market(s)

Local customers in Vero Beach, Florida.

Number of Pages Required

5+ page

Colors

Designer to choose colors to be used in the design.

Requirements
Must have
• Easy to navigate, attractive pages with pictures and logo, professional looking. must have my phone number and logo very prevalent and links to call or go to home page. I would like links to my social media accounts on the home page.
Nice to have
• Easy to navigate, attractive pages with pictures and logo, professional looking.

```html
<!DOCTYPE html>
<html lang="en">
<head>
<meta charset="utf-8">
<title>Keystone Mobile Detailing</title>
<link href="https://fonts.googleapis.com/css2?family=Lato:ital,wght@0,400;0,700;0,900;1,400&family=Montserrat:wght@700;800&display=swap" rel="stylesheet">
<style>
:root{
  --blue:#1ea4e6;
  --blue-dark:#0f7fc0;
  --ink:#333333;
  --heading:#555555;
  --text:#666666;
  --light:#f0f0f0;
  --white:#ffffff;
  --footer:#333333;
  --btn:#595959;
  --red:#e0473a;
}
*{box-sizing:border-box;margin:0;padding:0}
html,body{width:1200px;height:3854px;overflow:hidden}
body{position:relative;font-family:"Lato",sans-serif;color:var(--text);background:var(--white)}
.abs{position:absolute}
a{color:inherit;text-decoration:none}

/* top bar */
.topbar{left:0;top:0;width:1200px;height:36px;border-top:4px solid var(--blue);background:var(--white);font-size:14px;color:var(--ink)}
.topbar .contact{top:6px;display:flex;align-items:center;gap:8px}
.topbar .links{top:6px;font-size:14px}
.topbar .sep{top:4px;width:1px;height:22px;background:#ccc}
.social{top:0;width:36px;height:32px;background:var(--blue)}
.social span{position:absolute;left:12px;top:10px;width:12px;height:12px;border:2px solid var(--white);border-radius:2px}

/* header */
.header{left:0;top:36px;width:1200px;height:131px;background:var(--white);box-shadow:0 2px 6px rgba(0,0,0,.06)}
.brand{left:77px;top:22px;display:flex;align-items:center;gap:12px}
.brand .dot{width:58px;height:58px;border-radius:50%;background:var(--blue)}
.brand .name{font-family:"Lato",sans-serif;font-weight:900;color:var(--blue-dark);font-size:22px;line-height:1.1;width:180px}
.brand-phone{left:147px;top:96px;font-weight:900;font-size:16px;color:var(--red);letter-spacing:1px}
.nav{left:390px;top:58px;display:flex;gap:22px;font-size:17px;color:var(--ink)}
.nav .active{color:var(--red)}

/* hero */
.hero{left:0;top:167px;width:1200px;height:583px;overflow:hidden}
.hero .photo{position:absolute;inset:0;background:linear-gradient(110deg,#5b6068 0%,#8b9096 35%,#c3c6ca 60%,#6d737a 100%)}
.hero svg{position:absolute;left:0;top:0}
.hero h1{position:absolute;left:77px;top:405px;font-family:"Lato",sans-serif;font-weight:700;font-size:40px;line-height:56px;color:var(--white);width:620px}

/* about */
.about{left:0;top:750px;width:1200px;height:625px;background:var(--light)}
.h2{font-family:"Montserrat",sans-serif;font-weight:800;color:var(--heading);font-size:40px;letter-spacing:1px}
.about .h2{position:absolute;left:77px;top:125px}
.about p{position:absolute;left:77px;width:566px;font-size:15px;line-height:24px;color:var(--text)}
.btn{position:absolute;display:flex;height:47px;background:var(--btn);color:var(--white);font-weight:700;font-size:15px;align-items:center;border-radius:2px;overflow:hidden}
.btn .label{padding:0 18px}
.btn .arrow{width:47px;height:47px;background:var(--blue);display:flex;align-items:center;justify-content:center}
.about .frame{left:756px;top:83px;width:370px;height:401px;border:5px solid var(--blue)}
.about .pic{left:717px;top:126px;width:365px;height:414px;background:linear-gradient(160deg,#9fb1bf,#6d7f8c 55%,#c8cfd3)}

/* what we do */
.services{left:0;top:1375px;width:1200px;height:625px;background:var(--white)}
.center{position:absolute;left:0;width:1200px;text-align:center}
.card{position:absolute;top:115px;width:322px;height:417px;border:1px solid #dcdcdc;background:var(--white);text-align:center}
.card .icon{position:absolute;left:100px;top:42px;width:123px;height:123px;border-radius:50%;background:var(--blue);border:5px solid #d6eefb;box-shadow:0 0 0 2px var(--blue)}
.card .icon svg{position:absolute;left:24px;top:24px}
.card h3{position:absolute;left:0;top:195px;width:100%;font-weight:400;font-size:20px;color:var(--ink)}
.card p{position:absolute;left:28px;top:232px;width:266px;font-size:15px;line-height:24px}
.card .btn{left:72px;top:330px;height:40px}
.card .btn .arrow{width:40px;height:40px}

/* gallery */
.gallery{left:0;top:2000px;width:1200px;height:498px;background:linear-gradient(90deg,#3a2b22,#2c2a2b 30%,#2d3135 70%,#3b3025)}
.gallery .h2{color:var(--white)}
.shot{position:absolute;top:128px;height:301px}
.g-arrow{position:absolute;top:226px;width:42px;height:70px;background:rgba(0,0,0,.45);display:flex;align-items:center;justify-content:center}

/* testimonials */
.testimonials{left:0;top:2498px;width:1200px;height:483px;background:var(--light)}
.testimonials .quote{position:absolute;left:270px;top:123px;width:668px;text-align:center;font-style:italic;font-size:14px;line-height:24px}
.avatar{left:558px;top:219px;width:82px;height:82px;border-radius:50%;background:linear-gradient(#e9c9a8,#b98664);border:3px solid var(--white)}
.dots{position:absolute;left:567px;top:415px;display:flex;gap:12px}
.dots span{width:12px;height:12px;border-radius:50%;background:#999}
.dots span:first-child{background:var(--blue)}

/* blog */
.blog{left:0;top:2981px;width:1200px;height:527px;background:var(--white)}
.post{position:absolute;top:108px;width:323px;height:334px;border:1px solid #dcdcdc;background:var(--white)}
.post .img{position:absolute;left:0;top:0;width:100%;height:221px}
.post .date{position:absolute;left:18px;top:160px;width:72px;height:74px;background:var(--blue);color:var(--white);text-align:center}
.post .date b{display:block;font-size:30px;line-height:40px;margin-top:6px}
.post .date small{font-size:14px}
.post p{position:absolute;left:18px;top:258px;width:280px;font-size:18px;line-height:30px;color:var(--ink)}

/* footer */
.footer{left:0;top:3508px;width:1200px;height:296px;background:var(--footer);color:var(--white)}
.footer .brand{left:77px;top:44px}
.footer .brand .name{color:var(--white)}
.footer .fphone{position:absolute;left:147px;top:110px;font-weight:900;font-size:16px;letter-spacing:1px;color:var(--white)}
.footer h4{position:absolute;font-family:"Montserrat",sans-serif;font-weight:700;font-size:20px;letter-spacing:.5px}
.subscribe{left:77px;top:190px;width:291px;height:41px;border:1px solid #ccc;font-style:italic;font-size:15px;padding:10px 12px}
.subscribe svg{position:absolute;right:18px;top:11px}
.list{position:absolute;list-style:none;font-size:16px}
.list li{height:39px;display:flex;align-items:flex-start;gap:14px}
.list li i{width:12px;height:12px;border-radius:50%;background:var(--blue);margin-top:4px}
.copyright{left:0;top:3804px;width:1200px;height:50px;background:var(--blue);color:var(--white);font-size:15px;text-align:center;line-height:50px}
</style>
</head>
<body>

<!-- top bar -->
<div class="abs topbar">
  <div class="abs contact" style="left:77px">
    <svg width="16" height="12" viewBox="0 0 16 12"><rect x="1" y="1" width="14" height="10" fill="none" stroke="#1ea4e6" stroke-width="1.6"/><path d="M1 1l7 6 7-6" fill="none" stroke="#1ea4e6" stroke-width="1.6"/></svg>
    <a href="mailto:info@keystonemobiledetailing.com">info@keystonemobiledetailing.com</a>
  </div>
  <div class="abs contact" style="left:378px">
    <svg width="14" height="14" viewBox="0 0 24 24"><path d="M6.6 10.8a15 15 0 006.6 6.6l2.2-2.2a1 1 0 011-.25 11.4 11.4 0 003.6.6 1 1 0 011 1V20a1 1 0 01-1 1A17 17 0 013 4a1 1 0 011-1h3.5a1 1 0 011 1c0 1.25.2 2.45.6 3.6a1 1 0 01-.25 1z" fill="#1ea4e6"/></svg>
    <a href="tel:7725550148">772 555 0148</a>
  </div>
  <a class="abs links" style="left:838px" href="#">Shcedule</a>
  <div class="abs sep" style="left:918px"></div>
  <a class="abs links" style="left:940px" href="#">News</a>
  <a class="abs social" style="left:1012px" href="#" aria-label="Social page one"><span></span></a>
  <a class="abs social" style="left:1050px" href="#" aria-label="Social page two"><span></span></a>
  <a class="abs social" style="left:1088px" href="#" aria-label="Social page three"><span></span></a>
</div>

<!-- header -->
<header class="abs header">
  <a class="abs brand" href="#"><span class="dot"></span><span class="name">Keystone Mobile Detailing</span></a>
  <a class="abs brand-phone" href="tel:7725550148">772-555-0148</a>
  <nav class="abs nav">
    <a class="active" href="#">Home</a>
    <a href="#">About us</a>
    <a href="#">Car and Truck Detailing</a>
    <a href="#">Boat Detailing</a>
    <a href="#">Airplane Detailing</a>
    <a href="#">Contact Us</a>
  </nav>
</header>

<!-- hero -->
<section class="abs hero">
  <div class="photo" role="img" aria-label="Detailer polishing a car hood with a rotary buffer"></div>
  <svg width="1200" height="583" viewBox="0 0 1200 583">
    <path d="M0 345 C250 250 500 250 720 330 C900 395 1050 360 1200 300 L1200 583 L0 583 Z" fill="rgba(20,22,26,.72)"/>
    <path d="M0 345 C250 250 500 250 720 330 C900 395 1050 360 1200 300 L1200 318 C1050 380 900 415 720 352 C500 275 250 275 0 368 Z" fill="#1ea4e6"/>
    <path d="M0 310 C250 210 480 215 700 300" fill="none" stroke="#1ea4e6" stroke-width="6"/>
  </svg>
  <h1>Lorem Ipsum is simply dummy text of the printing.</h1>
</section>

<!-- about -->
<section class="abs about">
  <h2 class="h2">ABOUT US</h2>
  <p style="top:195px">Lorem Ipsum is simply dummy text of the printing and typesetting industry. Lorem Ipsum has been the industry's standard dummy text ever since the 1500s, when an unknown printer took a galley of type and scrambled it to make a type specimen book. It has survived not only five centuries, but also the leap into electronic typesetting, remaining essentially unchanged.</p>
  <p style="top:338px">Lorem Ipsum is simply dummy text of the printing and typesetting industry. Lorem Ipsum has been the industry's standard dummy text ever since the 1500s, when an unknown printer took a galley of type and scrambled it to make a type specimen bk.</p>
  <a class="btn" style="left:77px;top:437px" href="#"><span class="label">KNOW MORE</span><span class="arrow"><svg width="18" height="16" viewBox="0 0 18 16"><path d="M2 2l6 6-6 6M9 2l6 6-6 6" fill="none" stroke="#fff" stroke-width="2.4"/></svg></span></a>
  <div class="abs frame"></div>
  <div class="abs pic" role="img" aria-label="Detailer washing the deck of a boat"></div>
</section>

<!-- what we do -->
<section class="abs services">
  <h2 class="h2 center" style="top:42px">WHAT WE DO</h2>

  <div class="card" style="left:77px">
    <div class="icon"><svg width="65" height="65" viewBox="0 0 64 64"><path d="M8 14h48M14 14v8M50 14v8" stroke="#fff" stroke-width="3" fill="none"/><path d="M16 44l4-12h24l4 12v8H16z" fill="#fff"/><circle cx="23" cy="46" r="3" fill="#1ea4e6"/><circle cx="41" cy="46" r="3" fill="#1ea4e6"/></svg></div>
    <h3>Car and truck detailing</h3>
    <p>Lorem Ipsum is simply dummy text of the printing and typesetting industry. Lorem Ipsum has been the industry's standard.</p>
    <a class="btn" href="#"><span class="label">KNOW MORE</span><span class="arrow"><svg width="16" height="14" viewBox="0 0 18 16"><path d="M2 2l6 6-6 6M9 2l6 6-6 6" fill="none" stroke="#fff" stroke-width="2.4"/></svg></span></a>
  </div>

  <div class="card" style="left:439px">
    <div class="icon"><svg width="65" height="65" viewBox="0 0 64 64"><path d="M36 10l10 10-4 4-10-10z" fill="#fff"/><path d="M6 40h52l-8 12H14z" fill="#fff"/><path d="M18 40v-8h20v8" fill="#fff"/></svg></div>
    <h3>Boat detailing</h3>
    <p>Lorem Ipsum is simply dummy text of the printing and typesetting industry. Lorem Ipsum has been the industry's standard.</p>
    <a class="btn" href="#"><span class="label">KNOW MORE</span><span class="arrow"><svg width="16" height="14" viewBox="0 0 18 16"><path d="M2 2l6 6-6 6M9 2l6 6-6 6" fill="none" stroke="#fff" stroke-width="2.4"/></svg></span></a>
  </div>

  <div class="card" style="left:799px">
    <div class="icon"><svg width="65" height="65" viewBox="0 0 64 64"><path d="M8 30l48 4-4 6-16-1-12 12h-6l6-12-12-1-4 4H4l4-12z" fill="#fff"/><path d="M26 30l-6-14h6l12 14z" fill="#fff"/></svg></div>
    <h3>Airplane detailing</h3>
    <p>Lorem Ipsum is simply dummy text of the printing and typesetting industry. Lorem Ipsum has been the industry's standard.</p>
    <a class="btn" href="#"><span class="label">KNOW MORE</span><span class="arrow"><svg width="16" height="14" viewBox="0 0 18 16"><path d="M2 2l6 6-6 6M9 2l6 6-6 6" fill="none" stroke="#fff" stroke-width="2.4"/></svg></span></a>
  </div>
</section>

<!-- gallery -->
<section class="abs gallery">
  <h2 class="h2 center" style="top:52px">WORKING GALLERY</h2>
  <div class="shot" style="left:77px;width:242px;background:linear-gradient(#7fb3dd,#c9d6df 60%,#a7a9ab)" role="img" aria-label="Detailer washing a car in the sun"></div>
  <div class="shot" style="left:347px;width:239px;background:linear-gradient(135deg,#d9d9db,#8d949b 50%,#c78a8a)" role="img" aria-label="Gloved hand wiping a car headlight"></div>
  <div class="shot" style="left:614px;width:239px;background:linear-gradient(#dfe3e6,#9aa3a8 55%,#6f6f6c)" role="img" aria-label="Detailers cleaning a yacht hull"></div>
  <div class="shot" style="left:884px;width:239px;background:linear-gradient(#9cc4e6,#e2e4e6 45%,#9b8c78)" role="img" aria-label="Crew washing a private jet on the apron"></div>
  <div class="g-arrow" style="left:77px"><svg width="14" height="24" viewBox="0 0 14 24"><path d="M12 2L2 12l10 10" fill="none" stroke="#fff" stroke-width="2.5"/></svg></div>
  <div class="g-arrow" style="left:1081px"><svg width="14" height="24" viewBox="0 0 14 24"><path d="M2 2l10 10L2 22" fill="none" stroke="#fff" stroke-width="2.5"/></svg></div>
</section>

<!-- testimonials -->
<section class="abs testimonials">
  <h2 class="h2 center" style="top:45px">TESTIMONIALS</h2>
  <p class="quote">Lorem Ipsum is simply dummy text of the printing and typesetting industry. Lorem Ipsum has been the industry's standard dummy text ever since the 1500s, when an unknown printer took a galley of type and scrambled it to make a type specimen book. It has survived not only five centuries.</p>
  <div class="abs avatar" role="img" aria-label="Client portrait"></div>
  <div class="center" style="top:330px;font-size:19px;color:var(--ink)">- Client Name</div>
  <div class="center" style="top:366px;font-size:15px">Lorem Ipsum is simply.</div>
  <div class="dots"><span></span><span></span><span></span></div>
</section>

<!-- blog -->
<section class="abs blog">
  <h2 class="h2 center" style="top:42px">LATEST BLOG</h2>
  <article class="post" style="left:77px">
    <div class="img" style="background:linear-gradient(135deg,#2b2f35,#5a6068 50%,#7fb5c9)" role="img" aria-label="Hand washing a black car with a sponge"></div>
    <div class="date"><b>17</b><small>MAY</small></div>
    <p>Lorem Ipsum is simply dummy text of the printing.</p>
  </article>
  <article class="post" style="left:439px">
    <div class="img" style="background:linear-gradient(135deg,#b9a08a,#d8d8da 50%,#6b9fc4)" role="img" aria-label="Detailer spraying cleaner on a car"></div>
    <div class="date"><b>17</b><small>MAY</small></div>
    <p>Lorem Ipsum is simply dummy text of the printing.</p>
  </article>
  <article class="post" style="left:799px">
    <div class="img" style="background:linear-gradient(135deg,#3a3d42,#8c9298 55%,#c94a3a)" role="img" aria-label="Vacuuming a car interior"></div>
    <div class="date"><b>17</b><small>MAY</small></div>
    <p>Lorem Ipsum is simply dummy text of the printing.</p>
  </article>
</section>

<!-- footer -->
<footer class="abs footer">
  <a class="abs brand" href="#"><span class="dot"></span><span class="name">Keystone Mobile Detailing</span></a>
  <a class="fphone" href="tel:7725550148">772-555-0148</a>
  <h4 style="left:77px;top:158px;font-size:17px">SUBSCRIBE NEWSLETTER</h4>
  <div class="abs subscribe">Enter Email Address
    <svg width="20" height="18" viewBox="0 0 20 18"><path d="M1 8L19 1l-5 16-4-6z" fill="#fff"/></svg>
  </div>
  <h4 style="left:439px;top:52px">OUR SERVICES</h4>
  <ul class="list" style="left:446px;top:96px">
    <li><i></i>Car and truck detailing</li>
    <li><i></i>Boat detailing</li>
    <li><i></i>Airplane detailing</li>
  </ul>
  <h4 style="left:802px;top:52px">WORKING HOURS</h4>
  <ul class="list" style="left:802px;top:96px">
    <li>Monday to Friday - 10:00 to 5:00</li>
    <li>Saturday and Sunday - 10:00 to 5:00</li>
  </ul>
</footer>
<div class="abs copyright">©KEYSTONE Mobile Detailing - 2018. All Rights Reserved.</div>

</body>
</html>
```